Single Page Digital Brochure

We are a Sydney based finance company. We lend money to developers. Please see attached example of what we are looking to have produced. We just need a design which can be posted on LINKEDIN

Target Market(s)

Property Developers who are borrowing money

Industry/Entity Type

Finance

Requirements
Must have
• Australian relevant imagery.

TEXT TO INCLUDE:

New Offering from Ferngate Lending
Nice to have
• Design and colour scheme based around our logo (attached)

Please include the same text as the attachment

Please make the design based loosely on the attachment. But do not copy the attachement
Should not have
• Remove Text: 'Settle in under four days'

```html
<!DOCTYPE html>
<html lang="en">
<head>
<meta charset="utf-8">
<title>Ferngate Lending – New Offering</title>
<link rel="stylesheet" href="https://fonts.googleapis.com/css2?family=Montserrat:wght@300;400;500;600;700;800&display=swap">
<style>
  :root {
    --stage: #a7a5a6;
    --green-deep: #1b3528;
    --green: #244c38;
    --green-mid: #2f5a44;
    --white: #ffffff;
    --paper: #f1f1f1;
    --paper-dim: #dcdcdc;
    --ink: #3a3a3a;
  }
  * { box-sizing: border-box; margin: 0; padding: 0; }
  html, body {
    width: 1200px; height: 1200px; overflow: hidden;
    background: var(--stage);
    font-family: "Montserrat", sans-serif;
  }
  .brochure {
    position: absolute; left: 122px; top: 346px;
    width: 974px; height: 545px;
    overflow: hidden;
  }
  .side-offer {
    position: absolute; left: 0; top: 0; width: 482px; height: 545px;
    color: var(--white);
  }
  .side-offer .backdrop {
    position: absolute; inset: 0;
    background: linear-gradient(135deg, var(--green-mid) 0%, var(--green) 45%, var(--green-deep) 100%);
  }
  .brand {
    position: absolute; left: 52px; top: 80px;
    display: flex; align-items: center; gap: 8px;
    font-size: 12px; font-weight: 500; letter-spacing: 1.4px; text-transform: uppercase;
  }
  .brand-dot { width: 11px; height: 11px; border-radius: 50%; background: var(--white); }
  .offer-lead {
    position: absolute; left: 50px; top: 153px;
    font-size: 25px; font-weight: 600; letter-spacing: 0.3px;
  }
  .offer-name {
    position: absolute; left: 56px; top: 197px;
    font-size: 47px; font-weight: 800; line-height: 1; letter-spacing: 0.5px;
  }
  .offer-suffix {
    position: absolute; left: 56px; top: 251px;
    font-size: 46px; font-weight: 300; line-height: 1; letter-spacing: 0.5px;
  }
  .service-pill {
    position: absolute; left: 53px; top: 319px; width: 250px; height: 49px;
    border-radius: 25px; background: var(--white); color: var(--green);
    display: flex; align-items: center; justify-content: center;
    font-size: 18px; font-weight: 700; letter-spacing: 0.6px;
  }
  .service-list {
    position: absolute; left: 53px; top: 387px; width: 400px;
    font-size: 13.5px; font-weight: 400; line-height: 17px;
  }
  .web {
    position: absolute; left: 54px; top: 464px;
    display: flex; align-items: center; gap: 16px;
    font-size: 17px; letter-spacing: 1.8px; font-weight: 400;
  }
  .web b { font-weight: 600; }
  .side-deal {
    position: absolute; left: 482px; top: 0; width: 492px; height: 545px;
    color: var(--ink);
  }
  .side-deal .backdrop {
    position: absolute; inset: 0;
    background: linear-gradient(160deg, var(--paper-dim) 0%, var(--paper) 35%, #f6f6f6 70%, var(--paper-dim) 100%);
  }
  .headline {
    position: absolute; left: 55px; top: 44px; line-height: 1;
  }
  .headline .strong { display: block; font-size: 50px; font-weight: 800; color: var(--green); }
  .headline .soft { display: block; font-size: 51px; font-weight: 300; color: #2d2d2d; margin-top: 2px; }
  .deal-terms {
    position: absolute; left: 25px; top: 174px; list-style: none;
    font-size: 17px; font-weight: 400;
  }
  .deal-terms li { height: 39px; }
  .deal-terms b { font-weight: 700; }
  .call {
    position: absolute; left: 27px; top: 464px; height: 29px;
    display: flex; align-items: center; gap: 12px;
    font-size: 21px; font-weight: 700; color: #333;
  }
  .phone-pill {
    position: relative; height: 29px; width: 208px;
    border-radius: 15px; background: var(--green); color: var(--white);
    display: flex; align-items: center; padding-left: 37px;
    font-size: 19px; font-weight: 700; letter-spacing: 0.3px;
  }
  .phone-pill .icon {
    position: absolute; left: 0; top: -1px; width: 31px; height: 31px;
    border-radius: 50%; background: var(--white); border: 1.5px solid var(--green);
    display: flex; align-items: center; justify-content: center;
  }
</style>
</head>
<body>
  <main class="brochure">
    <section class="side-offer">
      <div class="backdrop" role="img" aria-label="Green-tinted upward view of Sydney CBD office towers"></div>
      <div class="brand"><span class="brand-dot"></span>Ferngate Lending</div>
      <p class="offer-lead">New Offering from</p>
      <h1 class="offer-name">FERNGATE</h1>
      <p class="offer-suffix">LENDING, INC.</p>
      <div class="service-pill">FINANCIAL SERVICES</div>
      <p class="service-list">Factor Financing, Accounts Receivable Financing, Purchase Order Financing, Contract Financing,Construction Financing, and Business Financing Attainment.</p>
      <div class="web">
        <svg width="24" height="28" viewBox="0 0 24 28" fill="none" stroke="#fff" stroke-width="1.6">
          <circle cx="12" cy="11" r="10"/>
          <ellipse cx="12" cy="11" rx="4.5" ry="10"/>
          <line x1="2" y1="11" x2="22" y2="11"/>
          <line x1="4" y1="5.5" x2="20" y2="5.5"/>
          <line x1="4" y1="16.5" x2="20" y2="16.5"/>
          <line x1="12" y1="21" x2="12" y2="26"/>
          <line x1="3" y1="26.5" x2="21" y2="26.5"/>
        </svg>
        <span>www.<b>ferngatelending</b>.com</span>
      </div>
    </section>

    <section class="side-deal">
      <div class="backdrop" role="img" aria-label="Soft grey Sydney desk scene with laptop keyboard and printed bar chart"></div>
      <h2 class="headline"><span class="strong">We did.</span><span class="soft">Just last week.</span></h2>
      <ul class="deal-terms">
        <li>Loan Amount: <b>$750,000</b></li>
        <li>Rate: <b>7.79%</b></li>
        <li>Term: <b>12 months</b></li>
        <li>LVR: <b>60%</b></li>
        <li>Repayments: <b>Capitalised</b></li>
        <li>Security: <b>2x Sydney Residential Propetties</b></li>
        <li>Purpose: <b>Business Working Capital</b></li>
      </ul>
      <div class="call">
        <span>Call Mara today on</span>
        <span class="phone-pill">
          <span class="icon">
            <svg width="16" height="16" viewBox="0 0 24 24" fill="#244c38">
              <path d="M6.6 10.8c1.4 2.8 3.8 5.1 6.6 6.6l2.2-2.2c.3-.3.7-.4 1-.2 1.1.4 2.3.6 3.6.6.6 0 1 .4 1 1V20c0 .6-.4 1-1 1C10.6 21 3 13.4 3 4c0-.6.4-1 1-1h3.5c.6 0 1 .4 1 1 0 1.3.2 2.5.6 3.6.1.3 0 .7-.2 1l-2.3 2.2z"/>
            </svg>
          </span>
          1-300-555-0187
        </span>
      </div>
    </section>
  </main>
</body>
</html>
```